Physiotherapiepraxis braucht Druckvorlage für Werbeanzeige
Zielgruppe
Dienstleistung im Gesundheitswesen als Physiotherapiepraxis.
Krankengymnastik, auch im häuslichen Bereich oder im Altersheim, und Massage sowie Wellnessanwendungen.
Zielgruppe sind primär Erwachsene, eingeschränkt auch Kinder.
Aufgabenstellung
Ich möchte eine Druckvorlage für eine Werbeanzeige, die ich immer mal wieder in verschiedenen Festschriften im dörflichen Bereich oder in einer regionalen Zeitschrift veröffentlichen kann.
Die Anzeige soll das Logo enthalten und die Anschrift der Praxis sowie die Telefonnummer und Adresse der Homepage.

```html
<!DOCTYPE html>
<html lang="de">
<head>
<meta charset="utf-8">
<title>Henrike Lammers – Physiotherapie</title>
<link rel="stylesheet" href="https://fonts.googleapis.com/css2?family=Kalam:wght@400&family=Open+Sans:wght@700&family=PT+Sans:wght@400&display=swap">
<style>
  :root {
    --green: #00773a;
    --gold: #d3b72b;
    --white: #ffffff;
    --frame: #8a8a8a;
  }
  html, body {
    margin: 0;
    padding: 0;
    overflow: hidden;
    background: var(--white);
  }
  .ad {
    position: relative;
    width: 1200px;
    height: 1200px;
    box-sizing: border-box;
    border: 3px solid var(--frame);
    background: var(--white);
    overflow: hidden;
  }
  .brand-name {
    position: absolute;
    left: 0;
    right: 0;
    top: 130px;
    margin: 0;
    text-align: center;
    font-family: "PT Sans", sans-serif;
    font-weight: 400;
    font-size: 88px;
    letter-spacing: 0.12em;
    line-height: 1;
    color: var(--green);
  }
  .service-band {
    position: absolute;
    left: 130px;
    top: 325px;
    width: 940px;
    height: 152px;
    background: var(--gold);
    display: flex;
    align-items: center;
    justify-content: center;
  }
  .service-band h2 {
    margin: 0;
    font-family: "Open Sans", sans-serif;
    font-weight: 700;
    font-size: 92px;
    letter-spacing: 0.01em;
    color: var(--white);
    line-height: 1;
  }
  .info-panel {
    position: absolute;
    left: 130px;
    top: 514px;
    width: 940px;
    height: 613px;
    background: var(--green);
  }
  .slogan {
    position: absolute;
    left: 30px;
    top: 40px;
    margin: 0;
    font-family: "Kalam", cursive;
    font-weight: 400;
    color: var(--white);
    line-height: 1.22;
    font-size: 96px;
    transform: rotate(-4deg);
    transform-origin: left top;
  }
  .slogan .line-two {
    display: block;
    padding-left: 110px;
  }
  .slogan .accent {
    color: var(--gold);
  }
  .contact-list {
    position: absolute;
    left: 0;
    top: 340px;
    margin: 0;
    padding: 0;
    list-style: none;
    font-family: "PT Sans", sans-serif;
    font-size: 60px;
    color: var(--white);
    line-height: 1;
  }
  .contact-list li {
    display: flex;
    align-items: center;
    height: 81px;
    padding-left: 14px;
  }
  .contact-list svg {
    width: 40px;
    height: 40px;
    margin-right: 14px;
    flex: none;
  }
</style>
</head>
<body>
  <main class="ad">
    <h1 class="brand-name">Henrike Lammers</h1>

    <div class="service-band">
      <h2>PHYSIOTHERAPIE</h2>
    </div>

    <section class="info-panel">
      <p class="slogan">Wir bringen Sie<span class="line-two"><span class="accent">gerne</span> in Bewegung!</span></p>

      <ul class="contact-list">
        <li>
          <svg viewBox="0 0 24 24" aria-hidden="true"><path fill="var(--gold)" d="M12 1.5c-4.4 0-8 3.4-8 7.8 0 5.8 8 13.2 8 13.2s8-7.4 8-13.2c0-4.4-3.6-7.8-8-7.8zm0 11a3.2 3.2 0 1 1 0-6.4 3.2 3.2 0 0 1 0 6.4z"/></svg>
          Lindenweg 7 in 21400 Moorheide
        </li>
        <li>
          <svg viewBox="0 0 24 24" aria-hidden="true"><path fill="var(--gold)" d="M6.6 2.5l3 3.6c.5.6.4 1.4-.1 1.9L7.8 9.6c1.3 2.8 3.7 5.2 6.6 6.6l1.6-1.7c.5-.5 1.3-.6 1.9-.1l3.6 3c.6.5.7 1.4.1 2l-1.8 2c-.8.8-2 1.1-3.1.7C9.9 19.8 4.2 14.1 1.9 7.3c-.4-1.1-.1-2.3.7-3.1l2-1.8c.6-.6 1.5-.5 2 .1z"/></svg>
          +49 (0) 4100 - 12 34 56
        </li>
        <li>
          <svg viewBox="0 0 24 24" aria-hidden="true">
            <circle cx="12" cy="12" r="10.5" fill="var(--gold)"/>
            <path fill="none" stroke="var(--green)" stroke-width="1.6" d="M1.5 12h21M12 1.5c3 3 4.3 6.5 4.3 10.5S15 19.5 12 22.5M12 1.5C9 4.5 7.7 8 7.7 12S9 19.5 12 22.5"/>
          </svg>
          www.physiotherapie-moorheide.de
        </li>
      </ul>
    </section>
  </main>
</body>
</html>
```